Velorik Cement

i need envelope a4 size and normal size - folder -paper bag - business card -
letterhead

Stationery Design project 'Stationery velorik cement : letterhead ,folder,business card ,envelope ,envelope A4size .paper bag '

Target Market(s)

ready mix concrete

Font styles to use
Serif

Colors

Designer to choose colors to be used in the design.

Requirements
Must have
• nice design

```html
<!DOCTYPE html>
<html lang="en">
<head>
<meta charset="utf-8">
<title>Velorik Cement – Business Card</title>
<link rel="stylesheet" href="https://fonts.googleapis.com/css2?family=Source+Serif+4:wght@400;600;700&family=Noto+Naskh+Arabic:wght@400;600&display=swap">
<style>
  :root {
    --brand-blue: #175a8c;
    --ink: #2a2a2a;
    --paper: #ffffff;
    --backdrop: #a7a7a7;
    --tagline-grey: #b9c3cc;
  }
  * { box-sizing: border-box; margin: 0; padding: 0; }
  html, body { width: 1200px; height: 950px; overflow: hidden; }
  body {
    background: var(--backdrop);
    font-family: "Source Serif 4", Georgia, serif;
    position: relative;
  }
  .card {
    position: absolute;
    width: 520px;
    height: 300px;
    box-shadow: 0 6px 14px rgba(0,0,0,0.25);
  }
  .card--front { left: 90px; top: 110px; background: var(--paper); }
  .card--back { left: 590px; top: 530px; background: var(--brand-blue); }

  .brand {
    position: absolute;
    display: flex;
    align-items: center;
    gap: 10px;
    font-weight: 700;
    letter-spacing: 0.04em;
    white-space: nowrap;
    line-height: 1;
  }
  .brand__dot { display: block; border-radius: 50%; flex: none; }
  .card--front .brand { right: 40px; top: 48px; color: var(--brand-blue); font-size: 30px; }
  .card--front .brand__dot { width: 18px; height: 18px; background: var(--brand-blue); }
  .card--back .brand {
    left: 50%; top: 118px; transform: translateX(-50%);
    color: var(--paper); font-size: 46px;
  }
  .card--back .brand__dot { width: 28px; height: 28px; background: var(--paper); }

  .tagline {
    position: absolute;
    letter-spacing: 0.03em;
    text-transform: uppercase;
    white-space: nowrap;
  }
  .card--front .tagline { right: 40px; top: 86px; color: var(--ink); font-size: 13px; }
  .card--back .tagline {
    left: 50%; top: 178px; transform: translateX(-50%);
    color: var(--tagline-grey); font-size: 18px;
  }

  .local-name {
    position: absolute;
    left: 40px; top: 104px;
    width: 200px;
    direction: rtl;
    text-align: right;
    font-family: "Noto Naskh Arabic", "Times New Roman", serif;
    font-size: 18px;
    line-height: 1.4;
    color: var(--ink);
  }
  .local-name__main { color: var(--brand-blue); font-weight: 600; }

  .person {
    position: absolute;
    right: 40px; top: 158px;
    text-align: right;
  }
  .person__name { color: var(--brand-blue); font-weight: 700; font-size: 18px; letter-spacing: 0.02em; line-height: 1.2; }
  .person__role { color: var(--ink); font-size: 12px; }

  .contact {
    position: absolute;
    left: 40px; bottom: 28px;
    font-size: 12px;
    line-height: 1.45;
    color: var(--ink);
  }
  .contact__address { margin-bottom: 8px; }
  .contact__label { color: var(--brand-blue); font-weight: 700; display: inline-block; width: 20px; }
</style>
</head>
<body>

  <section class="card card--front" aria-label="Business card front">
    <div class="brand"><span class="brand__dot"></span>VELORIK</div>
    <p class="tagline">Velorik Cement</p>

    <div class="local-name">
      <p class="local-name__main">کۆمپانیای ڤێلۆریک</p>
      <p>بۆ چیمەنتۆی ئامادەکراو</p>
    </div>

    <div class="person">
      <p class="person__name">DARAN HOLT</p>
      <p class="person__role">General Manager</p>
    </div>

    <div class="contact">
      <p class="contact__address">Industrial Zone No.7,<br>Riverside District</p>
      <p><span class="contact__label">T:</span>+964 (0) 750 418 3306</p>
      <p><span class="contact__label">E:</span>info@velorik-cement.com</p>
      <p><span class="contact__label">W:</span>www.velorik-cement.com</p>
    </div>
  </section>

  <section class="card card--back" aria-label="Business card back">
    <div class="brand"><span class="brand__dot"></span>VELORIK</div>
    <p class="tagline">Velorik Cement</p>
  </section>

</body>
</html>
```